Bramble Hollow Spirits Bottle Label

Bramble Hollow Spirits is a distillery and craft cocktail bar that will be located in Calgary, Alberta, Canada. Here, we create awesome hand crafted spirits like vodka, gin, rum, whiskey, brandy, liqueurs etc. We need bottle labels for 3 different initial products. The names of the products are as follows, Pepper Drift Gin (22% alc/vol), Moravel Dry Gin (40% alc/vol), and Talunet Contemporary Gin (40% alc/vol). It would be preferable to have 3 distinct labels. The alcohol by volume declaration must be on the front display of the label, without having to turn the bottle. There is a logo for Bramble Hollow Spirits I would like featured in the front around 1''x1" or 2.5cm x 2.5cm in size. Some last minute changes are being made to the logo so it is not uploaded at this moment. Abstract geometry would be a great fit for the contemporary gin and I have attached an example.Simple or complex designs both encouraged. The Pepper Drift Gin will be in the Moonea style bottle and the other two will be in Apotheker style bottles. Thank you so much to anyone interested in participating and we can't wait to hear from you. This is a great opportunity to showcase your creativity and be involved with future products!
Target Market(s)
Young professionals ages 21-30.

```html
<!DOCTYPE html>
<html lang="en">
<head>
<meta charset="utf-8">
<title>Bramble Hollow Spirits – Gin Labels</title>
<link rel="stylesheet" href="https://fonts.googleapis.com/css2?family=Abril+Fatface&family=Anton&family=Cinzel:wght@600&family=Great+Vibes&family=Montserrat:wght@600&family=Oswald:wght@500;700&family=Playfair+Display+SC:wght@700;900&display=swap">
<style>
  :root {
    --bg: #000000;
    --slate: #5d8ca9;
    --slate-light: #7aa3ba;
    --gold: #c9a24a;
    --gold-light: #f1dc94;
    --cream: #f6f1e4;
    --green: #2f6d4b;
    --copper: #c4612a;
    --copper-light: #e89a5c;
    --ink: #1c1714;
    --white: #ffffff;
  }
  * { box-sizing: border-box; margin: 0; padding: 0; }
  html, body { width: 1200px; height: 1200px; overflow: hidden; background: var(--bg); }
  .canvas { position: relative; width: 1200px; height: 1200px; background: var(--bg); }
  .label { position: absolute; }
  .label svg { position: absolute; left: 0; top: 0; }
  .abs { position: absolute; }
  .center { left: 0; right: 0; text-align: center; }

  /* Pepper Drift */
  .pepper { left: 54px; top: 152px; width: 520px; height: 518px; }
  .pepper .brand { top: 80px; font-family: "Cinzel", serif; font-weight: 600; font-size: 15px; line-height: 18px; color: var(--gold-light); letter-spacing: 0.5px; }
  .pepper .tagline { top: 200px; font-family: "Montserrat", sans-serif; font-weight: 600; font-size: 9px; line-height: 12px; letter-spacing: 1px; color: var(--gold-light); }
  .pepper .name { top: 214px; font-family: "Cinzel", serif; font-weight: 600; font-size: 46px; line-height: 52px; color: var(--cream); text-shadow: 0 1px 2px rgba(0,0,0,.35); }
  .pepper .script { top: 278px; font-family: "Great Vibes", cursive; font-size: 80px; color: var(--white); line-height: 80px; text-shadow: 0 1px 2px rgba(0,0,0,.3); }
  .pepper .volume { top: 374px; left: 70px; font-family: "Oswald", sans-serif; font-weight: 700; font-size: 17px; line-height: 20px; color: var(--cream); }
  .pepper .abv { top: 374px; right: 70px; font-family: "Oswald", sans-serif; font-weight: 700; font-size: 17px; line-height: 20px; color: var(--cream); }
  .pepper .craft { top: 414px; font-family: "Playfair Display SC", serif; font-weight: 900; font-size: 18px; line-height: 20px; letter-spacing: 1px; color: var(--cream); }
  .pepper .batch { top: 435px; font-family: "Montserrat", sans-serif; font-weight: 600; font-size: 10px; line-height: 13px; letter-spacing: 1px; color: var(--gold-light); }
  .pepper .origin { top: 449px; font-family: "Oswald", sans-serif; font-weight: 700; font-size: 12px; line-height: 15px; color: var(--cream); }

  /* Moravel */
  .moravel { left: 604px; top: 122px; width: 500px; height: 612px;
    clip-path: polygon(0 0,100% 0,100% 100%,90% 97.5%,75% 96.5%,60% 97%,45% 95.8%,30% 96.6%,15% 96%,5% 97.6%,0 98.2%); }
  .moravel .panel { position: absolute; left: 0; right: 0; }
  .moravel .green { background: var(--green); }
  .moravel .white { background: var(--white); }
  .moravel .band { background: linear-gradient(var(--white) 0 15%, var(--copper) 15% 85%, var(--white) 85%); }
  .moravel .brand { top: 72px; font-family: "Playfair Display SC", serif; font-weight: 700; font-size: 19px; line-height: 24px; color: var(--copper-light); letter-spacing: 0.5px; }
  .moravel .name { top: 168px; font-family: "Abril Fatface", serif; font-size: 74px; color: var(--ink); letter-spacing: 1px; text-shadow: 2px 2px 2px rgba(0,0,0,.25); line-height: 80px; }
  .moravel .kind { top: 288px; font-family: "Playfair Display SC", serif; font-weight: 900; font-size: 31px; line-height: 36px; letter-spacing: 4px; color: var(--copper); }
  .moravel .craft { top: 366px; font-family: "Montserrat", sans-serif; font-weight: 600; font-size: 22px; line-height: 26px; letter-spacing: 6px; color: var(--ink); }
  .moravel .premium { top: 394px; font-family: "Playfair Display SC", serif; font-weight: 900; font-size: 20px; line-height: 24px; letter-spacing: 2px; color: var(--copper); }
  .moravel .batch { top: 426px; font-family: "Montserrat", sans-serif; font-weight: 600; font-size: 11px; line-height: 14px; letter-spacing: 3px; color: var(--ink); }
  .moravel .blurb { top: 498px; font-family: "Oswald", sans-serif; font-weight: 700; font-size: 19px; letter-spacing: 1.5px; line-height: 24px; color: var(--white); }
  .moravel .spec { top: 552px; font-family: "Oswald", sans-serif; font-weight: 500; font-size: 13px; line-height: 16px; letter-spacing: 2px; color: var(--copper-light); }

  /* Talunet */
  .talunet { left: 328px; top: 774px; width: 468px; height: 378px; overflow: hidden; }
  .talunet .field { position: absolute; inset: 0;
    background:
      radial-gradient(circle at 55% 55%, rgba(246,205,150,.9) 0, rgba(246,205,150,0) 35%),
      linear-gradient(200deg, #7b3a9c 0%, #5a6fb8 18%, rgba(90,111,184,0) 40%),
      linear-gradient(330deg, #6aa9dc 0%, #b7c6e0 20%, rgba(183,198,224,0) 40%),
      linear-gradient(120deg, #d9236e 0%, #e05a6a 35%, #ef8c6a 60%, #e36f7e 100%); }
  .talunet .brand { top: 58px; left: 296px; width: 160px; text-align: center; font-family: "Oswald", sans-serif; font-weight: 500; font-size: 17px; line-height: 22px; color: #4a3414; }
  .talunet .copy { left: 34px; top: 226px; font-family: "Oswald", sans-serif; font-weight: 500; font-size: 17px; line-height: 28px; color: var(--white); transform: scaleX(.75); transform-origin: left; text-transform: uppercase; white-space: nowrap; text-shadow: 1px 1px 1px rgba(0,0,0,.3); }
  .talunet .spec { left: 310px; top: 300px; font-family: "Oswald", sans-serif; font-weight: 500; font-size: 15px; line-height: 21px; color: var(--white); transform: scaleX(.7); transform-origin: left; white-space: nowrap; }
</style>
</head>
<body>
<main class="canvas">

  <!-- Pepper Drift Gin -->
  <section class="label pepper">
    <svg width="520" height="518" viewBox="0 0 520 518">
      <defs>
        <linearGradient id="slate" x1="0" y1="0" x2="1" y2="1">
          <stop offset="0" stop-color="#7ea7be"/><stop offset="1" stop-color="#4f82a0"/>
        </linearGradient>
      </defs>
      <path d="M70,20 Q260,-5 450,20 Q510,28 515,90 Q525,259 515,428 Q510,490 450,498 Q260,523 70,498 Q10,490 5,428 Q-5,259 5,90 Q10,28 70,20Z" fill="url(#slate)"/>
      <path d="M80,42 Q260,20 440,42 Q490,50 494,100 Q502,259 494,418 Q490,468 440,476 Q260,500 80,476 Q30,468 26,418 Q18,259 26,100 Q30,50 80,42Z" fill="none" stroke="var(--gold)" stroke-width="3"/>
      <g fill="var(--gold-light)" opacity=".35">
        <ellipse role="img" aria-label="Gold scroll ornament" cx="102" cy="122" rx="34" ry="26"/>
        <ellipse role="img" aria-label="Gold scroll ornament" cx="418" cy="122" rx="34" ry="26"/>
        <ellipse role="img" aria-label="Gold scroll ornament" cx="102" cy="420" rx="34" ry="26"/>
        <ellipse role="img" aria-label="Gold scroll ornament" cx="418" cy="420" rx="34" ry="26"/>
        <rect role="img" aria-label="Gold flourish divider" x="160" y="146" width="200" height="30" rx="15"/>
        <rect role="img" aria-label="Gold flourish" x="92" y="306" width="100" height="14" rx="7"/>
        <rect role="img" aria-label="Gold flourish" x="328" y="306" width="100" height="14" rx="7"/>
      </g>
    </svg>
    <div class="abs center brand">Bramble Hollow Spirits</div>
    <div class="abs center tagline">BOTANICALS CAREFULY SELECTED</div>
    <div class="abs center name">PEPPER DRIFT</div>
    <div class="abs center script">Gin</div>
    <div class="abs volume">750CL</div>
    <div class="abs abv">22%ALC.VOL</div>
    <div class="abs center craft">HANDCRAFT</div>
    <div class="abs center batch">SMALL BATCH DISTILLED</div>
    <div class="abs center origin">PRODUCT OF CANADA</div>
  </section>

  <!-- Moravel Dry Gin -->
  <section class="label moravel">
    <div class="panel green" style="top:0;height:142px"></div>
    <div class="panel band" role="img" aria-label="Copper patterned border" style="top:142px;height:16px"></div>
    <div class="panel white" style="top:158px;height:100px"></div>
    <div class="panel band" role="img" aria-label="Copper patterned border" style="top:258px;height:16px"></div>
    <div class="panel green" style="top:274px;height:66px"></div>
    <div class="panel band" role="img" aria-label="Copper patterned border" style="top:340px;height:16px"></div>
    <div class="panel white" style="top:356px;height:96px"></div>
    <div class="panel band" role="img" aria-label="Copper patterned border" style="top:452px;height:16px"></div>
    <div class="panel green" style="top:468px;height:144px"></div>
    <svg width="500" height="612" viewBox="0 0 500 612">
      <g fill="var(--copper)" opacity=".55">
        <ellipse role="img" aria-label="Copper leaf sprig ornament" cx="52" cy="78" rx="38" ry="44"/>
        <ellipse role="img" aria-label="Copper leaf sprig ornament" cx="448" cy="78" rx="38" ry="44"/>
        <ellipse role="img" aria-label="Copper leaf sprig ornament" cx="52" cy="532" rx="38" ry="44"/>
        <ellipse role="img" aria-label="Copper leaf sprig ornament" cx="448" cy="532" rx="38" ry="44"/>
      </g>
    </svg>
    <div class="abs center brand">Bramble Hollow Spirits</div>
    <div class="abs center name">MORAVEL</div>
    <div class="abs center kind">DRY GIN</div>
    <div class="abs center craft">HANDCRAFT</div>
    <div class="abs center premium">PREMIUM</div>
    <div class="abs center batch">SMALL BATCH SPIRIT</div>
    <div class="abs center blurb">DISTINTIVE COMBINATION OF<br>BOTANICAL PRODUCTS</div>
    <div class="abs center spec">40% ALC / VOL · 750CL</div>
  </section>

  <!-- Talunet Contemporary Gin -->
  <section class="label talunet">
    <div class="field" role="img" aria-label="Abstract low-poly geometric pattern in pink, orange, peach, violet and blue"></div>
    <div class="abs brand">Bramble Hollow Spirits</div>
    <svg width="468" height="378" viewBox="0 0 468 378">
      <defs>
        <linearGradient id="metal" x1="0" y1="0" x2="0" y2="1">
          <stop offset="0" stop-color="#6b5524"/><stop offset=".5" stop-color="#2a1f0c"/><stop offset="1" stop-color="#7a6230"/>
        </linearGradient>
      </defs>
      <text x="30" y="122" textLength="150" lengthAdjust="spacingAndGlyphs" font-family="Anton, sans-serif" font-size="66" fill="var(--white)" stroke="#c9c9c9" stroke-width=".5">TALUNET</text>
      <text x="30" y="208" textLength="404" lengthAdjust="spacingAndGlyphs" font-family="Anton, sans-serif" font-size="100" fill="url(#metal)" stroke="var(--gold-light)" stroke-width="1">CONTEMPORARY</text>
      <text x="304" y="258" textLength="124" lengthAdjust="spacingAndGlyphs" font-family="Playfair Display SC, serif" font-weight="700" font-size="64" fill="url(#metal)">GIN</text>
    </svg>
    <div class="abs copy">We use carefuly botanicals<br>selectes from around the globe</div>
    <div class="abs spec">40% ALC / VOL<br>750CL</div>
  </section>

</main>
</body>
</html>
```